Template design for organic gardening site for ShopVantra platform

We need a template design for our new 'Fen Leaf Naturals' shopvantra site. Fen Leaf Naturals specialises in organic nutrients for gardening plus all equipment needed to grow.
Domain name will be www.fenleafnaturals.co.uk
Colours used should include logo colours, see attached image. Other colours to compliment the greens and lift the feel of the site could be yellow or orange.
Home page design should include, but not limited to the following:
Interactive banner carousel space
A smaller banner advertising space
Featured products
New products
Sale products feature/link
Articles links/feature
+ all standard shopvantra features such as menus, etc
The site will be selling products (these are nutrients) such as:
Pelvarimost
Marsh hare soil tonic
Terrawix
Nuro pods
Stem triumph
Sprout charm
Vel
Flint amber
Moswelder
+ more products and brands
Site layouts we like include:
www.tidemarkaquafarm.co.uk ... A bit old fashioned but cool
www.lanternbeds.co.uk ... Nice but too compact
www.flintamber.com ... Has a nice top half
www.sponsorapod.org.uk ... Nice colours and header
www.penhurstplants.co.uk ... nice layout, but needs image carousel
www.wrenmeal.co.uk ... Nice background and colours
www.thistle.co.uk ... Nice colours and layout
www.danielmorrowhorticulture.com ... Nice layout and header
www.sprivant.co.uk ... Cool colours and shop pages layout is nice
www.aquavenor.co.uk ... One of the best layouts
The site should feel clean, modern and elegant.
Target Market(s)
Indoor and outdoor organic gardeners
Look and feel

```html
<!DOCTYPE html>
<html lang="en">
<head>
<meta charset="utf-8">
<title>Fen Leaf Naturals</title>
<link href="https://fonts.googleapis.com/css2?family=PT+Sans:wght@400;700&family=PT+Sans+Narrow:wght@700&display=swap" rel="stylesheet">
<style>
  :root {
    --page-bg: #f3f3f2;
    --leaf: #6b8c1d;
    --leaf-dark: #4f7a2c;
    --logo-green: #5e9a2e;
    --nav-green: #4f8a3c;
    --white: #ffffff;
    --hero-dark: #3a4a22;
  }
  * { margin: 0; padding: 0; box-sizing: border-box; }
  html, body { width: 1200px; height: 875px; overflow: hidden; }
  body {
    position: relative;
    background: var(--page-bg);
    font-family: "PT Sans", sans-serif;
    color: var(--white);
  }
  .brand { position: absolute; left: 182px; top: 28px; display: flex; align-items: center; gap: 9px; }
  .brand-mark { width: 64px; height: 64px; background: var(--leaf-dark); border-radius: 6px; }
  .brand-name {
    font-family: "PT Sans Narrow", sans-serif; font-weight: 700; font-size: 31px;
    line-height: 32px; color: var(--logo-green); text-transform: uppercase;
  }
  .account-link { position: absolute; right: 183px; top: 10px; font-size: 8.5px; color: var(--nav-green); }
  .search {
    position: absolute; left: 874px; top: 36px; width: 143px; height: 23px;
    border: 1px solid var(--leaf); border-radius: 5px; background: var(--white);
    font-size: 8px; color: #555; padding: 6px 10px;
  }
  .search svg { position: absolute; right: 7px; top: 3px; }
  .main-nav { position: absolute; right: 183px; top: 70px; display: flex; gap: 16px; }
  .main-nav a { color: var(--nav-green); text-decoration: none; font-size: 19px; }
  .hero {
    position: absolute; left: 0; top: 116px; width: 1200px; height: 415px;
    background: linear-gradient(90deg, #4b5d2a 0%, #3c4a25 35%, #2f3a1f 60%, #3f5526 85%, #557a2e 100%);
  }
  .hero-arrow { position: absolute; top: 188px; }
  .hero-title {
    position: absolute; left: 464px; top: 76px; font-size: 57px; line-height: 63px;
    font-weight: 400; letter-spacing: -0.5px;
  }
  .hero-text { position: absolute; left: 465px; top: 214px; width: 490px; font-size: 10.5px; line-height: 13px; }
  .hero-button {
    position: absolute; left: 465px; top: 272px; width: 129px; height: 39px;
    border: 1px solid var(--white); border-radius: 4px; font-size: 15px;
    display: flex; align-items: center; justify-content: center;
  }
  .hero-dots { position: absolute; left: 559px; top: 372px; display: flex; gap: 7px; }
  .hero-dots span { width: 12px; height: 12px; border-radius: 50%; background: var(--leaf); }
  .hero-dots span.active { background: var(--hero-dark); border: 2px solid var(--leaf); }
  .side-panel { position: absolute; left: 173px; width: 209px; background: var(--leaf); padding: 0 0 0 9px; }
  .side-panel.shop { top: 116px; height: 271px; }
  .side-panel.brands { top: 396px; height: 135px; }
  .side-panel h2 {
    font-weight: 400; font-size: 19px; margin: 11px 0 0 2px; padding-bottom: 9px;
    width: 142px; border-bottom: 1px solid var(--white);
  }
  .side-panel ul { list-style: none; margin-top: 10px; }
  .side-panel li { font-size: 15px; line-height: 22.5px; }
  .card { position: absolute; top: 577px; width: 200px; height: 262px; border: 1px solid var(--leaf); }
  .card-head {
    height: 36px; background: var(--leaf); display: flex; align-items: center;
    justify-content: center; gap: 16px; font-size: 15px; padding-left: 14px;
  }
  .card-photo { height: 225px; }
</style>
</head>
<body>
  <header>
    <div class="brand">
      <div class="brand-mark"></div>
      <div class="brand-name">Fen Leaf<br>Naturals</div>
    </div>
    <div class="account-link">Sign in / Register</div>
    <div class="search">search
      <svg width="15" height="16" viewBox="0 0 15 16"><circle cx="6" cy="6" r="4.8" fill="none" stroke="#4f7a2c" stroke-width="1.4"/><line x1="9.5" y1="9.7" x2="14" y2="14.5" stroke="#4f7a2c" stroke-width="1.8"/></svg>
    </div>
    <nav class="main-nav">
      <a>Home</a><a>About us</a><a>Products</a><a>Beauty advice</a><a>Contact us</a>
    </nav>
  </header>

  <section class="hero" role="img" aria-label="Garden scene with green rubber boots, watering can, pots and flowers">
    <svg class="hero-arrow" style="left:44px" width="18" height="28" viewBox="0 0 18 28"><polyline points="15,2 3,14 15,26" fill="none" stroke="#fff" stroke-width="3"/></svg>
    <svg class="hero-arrow" style="left:1144px;top:191px" width="18" height="28" viewBox="0 0 18 28"><polyline points="3,2 15,14 3,26" fill="none" stroke="#fff" stroke-width="3"/></svg>
    <h1 class="hero-title">CREATING PLACES OF<br>LASTING BEAUTY</h1>
    <p class="hero-text">Duis autem vel eum iriure dolor in hendrerit in vulputate velit esse molestie consequat, vel illum dolore eu feugiat nulla facilisis at vero eros et accumsan et iusto odio dignissim qui blandi</p>
    <div class="hero-button">more about</div>
    <div class="hero-dots"><span class="active"></span><span></span><span></span><span></span><span></span></div>
  </section>

  <aside class="side-panel shop">
    <h2>Shop for</h2>
    <ul>
      <li>Pelvarimost</li><li>Marsh hare soil tonic</li><li>Terrawix</li><li>Nuro pods</li>
      <li>Stem triumph</li><li>Sprout charm</li><li>Vel</li><li>Flint amber</li><li>Moswelder</li>
    </ul>
  </aside>
  <aside class="side-panel brands">
    <h2>Brands</h2>
    <ul><li>Pelvarimost</li><li>Marsh hare soil tonic</li><li>Terrawix</li></ul>
  </aside>

  <section class="featured">
    <div class="card" style="left:182px">
      <div class="card-head">Flint amber <svg width="11" height="18" viewBox="0 0 11 18"><polyline points="2,2 9,9 2,16" fill="none" stroke="#fff" stroke-width="2.4"/></svg></div>
      <div class="card-photo" role="img" aria-label="Gloved hand scattering granules beside a seedling in soil" style="background:linear-gradient(135deg,#4d4636,#6b7f3a 55%,#7cc13a)"></div>
    </div>
    <div class="card" style="left:394px">
      <div class="card-head">Stem triumph <svg width="11" height="18" viewBox="0 0 11 18"><polyline points="2,2 9,9 2,16" fill="none" stroke="#fff" stroke-width="2.4"/></svg></div>
      <div class="card-photo" role="img" aria-label="Backpack leaf blower on paving stones" style="background:linear-gradient(135deg,#8a8c8f,#b7b8ba 50%,#d9d6d0)"></div>
    </div>
    <div class="card" style="left:606px">
      <div class="card-head">Pelvarimost <svg width="11" height="18" viewBox="0 0 11 18"><polyline points="2,2 9,9 2,16" fill="none" stroke="#fff" stroke-width="2.4"/></svg></div>
      <div class="card-photo" role="img" aria-label="Gloved hands holding soil with a young plant" style="background:linear-gradient(160deg,#4f6b3a,#9c9a8e 50%,#7a4e2c)"></div>
    </div>
    <div class="card" style="left:818px">
      <div class="card-head">Sprout charm <svg width="11" height="18" viewBox="0 0 11 18"><polyline points="2,2 9,9 2,16" fill="none" stroke="#fff" stroke-width="2.4"/></svg></div>
      <div class="card-photo" role="img" aria-label="Gardener in overalls with a backpack pressure sprayer" style="background:linear-gradient(135deg,#5a8fd0,#6f9bd6 50%,#2b3550)"></div>
    </div>
  </section>
</body>
</html>
```